Design Contest: A New Look & Feel for VORMI.nl

🌍 Context
VORMI.nl combines knowledge about supplements, ingredients, and spirituality, while also offering lectures, retreats, and training programs.
We are not a foundation or donation platform, but an open knowledge network with a professional, warm, and trustworthy presence.

Our mission is to connect science and soul, sharing valuable insights and experiences that inspire both rational understanding and spiritual growth.

🎯 The Goal
We’re inviting talented web designers and visual creatives to redesign VORMI.nl into a modern, elegant, and emotionally resonant platform.

The new design should communicate:
Warmth and human connection,
Professionalism and clarity, and
A sense of discovery and inspiration.
The site will serve as a central hub for education, community, and conscious travel β€” bridging science, nature, and spirituality.

Landing Page (One-Pager):

A welcoming introduction to VORMI that immediately conveys our essence: knowledge, connection, and inspiration.
Visually guides visitors toward our main areas β€” journeys, education, and knowledge β€” with clear calls to action.

Travel Page Design:

A dedicated layout for a spiritual journey or retreat
Should evoke curiosity, emotion, and trust β€” encouraging visitors to read the program and feel inspired to book.

Education Page Design:
A page for one specific training or lecture.
Should look professional and engaging, highlighting benefits and making visitors eager to sign up.

Ingredient Page Design:
A clean, structured layout for an ingredient (e.g., Velotrin K7 Matrix®).
Should balance science and accessibility β€” informative yet visually appealing, showing related insights or products.

✨ What We’re Looking For
🌸 Warm, Friendly Aesthetic
A soft, grounded color palette (see moodboard below).
A look that feels welcoming, safe, modern, and inspiring.
Avoid harsh contrasts or corporate coldness β€” aim for organic elegance and heart-centered design.

🌿 Clean, Airy Layout
Generous white/cream space for readability and calm.
Rounded corners, smooth transitions, and balanced composition.
Use light textures (paper, waves, or organic shapes) to evoke warmth.

✍️ Modern Typography
Body text: Nunito, Lato, or Raleway β€” friendly, clear, and easy to read.
Headings: Playfair Display or Quicksand β€” elegant and expressive.
Typography should reflect both expertise and approachability.

πŸ”— Clear Navigation
Logical, intuitive structure with the following key areas:
Knowledge Hub – Products – Activities – About – Contact
Clear, soft-toned buttons and navigation encouraging exploration.
Consider β€œrelated content” cards or visual pathways connecting knowledge, events, and products.

πŸ’« Visual Integration
Create visual links between knowledge, activities, and products (e.g., tags, badges, or modular cards).
Filters or category highlights to navigate supplement/ingredient content easily.
Visual flow should feel alive yet harmonious.

🧠 Local & Human Connection
Photography that emphasizes real people, learning moments, and connection with nature.
Avoid clinical or corporate stock images β€” show authenticity, empathy, and light.

🀝 Community Features
Dedicated space for reviews, expert Q&A, or interaction.
These areas should radiate trust, safety, and a sense of belonging.

🧩 Brisk CMS Compatibility
Must be responsive and easily built within Brisk CMS (drag-and-drop).
Show where dynamic content (articles, events, or journeys) will be placed and how cards adapt to different devices.

🎨 Moodboard & Color Palette
Color Name HEX Code Emotion & Use
Warm Beige #DFBAAA The grounding base color β€” evokes natural warmth, balance, and calm. Ideal for backgrounds and section dividers.
Light Cream #F5EAE5 Airy and gentle β€” conveys purity, openness, and readability. Use for backgrounds and whitespace.
Deep Aubergine #431624 Adds depth and mystery β€” perfect for headlines, highlights, or footers. Symbolizes introspection and wisdom.
Wine Red #750E2B Expresses vitality, heart energy, and focus. Ideal for buttons, accents, or key highlights.
Burnt Orange #F26C2E Brings creative spark and positivity. Great for hover states, subtle icons, or energetic accents.
Mustard Yellow #B68620 Symbolizes light, optimism, and knowledge. Use as a secondary accent or highlight.

Color philosophy:
This palette represents the meeting point between Earth and Fire β€” grounding warmth combined with vibrant inspiration.
It visually communicates the essence of VORMI: trustworthy science, human connection, and transformative energy.

🧠 Target Audience
Health professionals and therapists seeking supplement and ingredient education.
Consumers and conscious individuals interested in wellbeing, spirituality, and science.
Spiritual explorers looking for transformative journeys and community learning.

πŸ’‘ Functional & Structural Goals
The site should clearly showcase VORMI’s four pillars:
Journeys & Retreats – spiritual travel experiences.
Academy & Trainings – professional education and lectures.
Knowledge Center – accessible supplement & ingredient knowledge (scientific yet warm).

πŸ“¦ What to Submit
A homepage concept (desktop + mobile).
Final delivery as a layererd PSD

```html
<!DOCTYPE html>
<html lang="en">
<head>
<meta charset="utf-8">
<title>VORMI – Advancement of People and Organization</title>
<link href="https://fonts.googleapis.com/css2?family=Playfair+Display:wght@400;500;600;700&family=Nunito:wght@400;500;600;700;800&display=swap" rel="stylesheet">
<style>
:root{
  --wine:#750E2B;
  --aubergine:#431624;
  --orange:#F26C2E;
  --cream:#F5EAE5;
  --beige:#DFBAAA;
  --text:#3a2a2e;
  --muted:#8a7c7f;
  --white:#ffffff;
  --field:#e9dcd7;
  --footer-bg:#f7eeea;
}
*{box-sizing:border-box;margin:0;padding:0}
html,body{width:1200px;height:4101px;overflow:hidden}
body{position:relative;background:var(--white);font-family:'Nunito',sans-serif;color:var(--text)}
.abs{position:absolute}
.serif{font-family:'Playfair Display',serif}
.btn{position:absolute;display:flex;align-items:center;justify-content:center;border-radius:30px;color:var(--white);font-family:'Playfair Display',serif;font-weight:600;font-size:16px}
.btn-wine{background:var(--wine)}
.btn-orange{background:var(--orange)}

/* header */
.brand{position:absolute;left:49px;top:28px;display:flex;align-items:center;gap:12px}
.brand-dot{width:40px;height:40px;border-radius:50%;background:var(--wine)}
.brand-name{font-family:'Nunito',sans-serif;font-weight:800;color:var(--wine);font-size:26px;line-height:26px;letter-spacing:1px}
.nav{position:absolute;top:42px;left:592px;display:flex;gap:39px;font-size:14px;color:var(--muted)}
.nav .active{color:var(--wine);text-decoration:underline;text-underline-offset:4px}

/* hero */
.hero{left:83px;top:97px;width:1028px;height:562px;background:linear-gradient(180deg,#3b3547 0%,#8a5a4e 28%,#c98c6b 38%,#5a6f7c 55%,#2d3f4a 100%)}
.hero-title{position:absolute;left:0;width:1200px;top:290px;text-align:center;color:var(--white);font-family:'Playfair Display',serif;font-weight:600;font-size:54px;line-height:67px}
.hero-sub{position:absolute;left:0;width:1200px;top:440px;text-align:center;color:var(--white);font-size:15px;line-height:21px}

/* section headings */
.h-center{position:absolute;left:0;width:1200px;text-align:center;font-family:'Playfair Display',serif;color:var(--aubergine)}
.p-center{position:absolute;left:0;width:1200px;text-align:center;font-size:14.5px;line-height:22px;color:#4e4346}

/* services */
.service{position:absolute;top:923px;width:263px;height:172px;background:var(--white);box-shadow:0 6px 18px rgba(67,22,36,.12)}
.service-icon{position:absolute;left:23px;top:-34px;width:57px;height:57px;border-radius:50%;background:var(--orange);display:flex;align-items:center;justify-content:center;box-shadow:0 4px 10px rgba(242,108,46,.35)}
.service h3{position:absolute;left:23px;top:45px;font-weight:400;font-size:19px;color:var(--text)}
.service p{position:absolute;left:23px;top:84px;width:190px;font-size:9.5px;line-height:13px;color:#9a8e90}
.service .more{position:absolute;right:0;bottom:0;width:82px;height:32px;background:var(--cream);font-size:10px;color:var(--wine);display:flex;align-items:center;justify-content:center}

/* about */
.about{left:0;top:1268px;width:1200px;height:580px;background:var(--cream)}
.about-photo{left:49px;top:1346px;width:449px;height:417px;border-top-right-radius:260px 300px;background:radial-gradient(circle at 55% 50%,#f0a6c3 0%,#e8b6c6 30%,#bcd7c9 70%,#8fbfbf 100%)}
.about h2{position:absolute;left:594px;top:48px;font-size:38px;color:var(--aubergine)}
.about .rule{position:absolute;left:594px;top:121px;width:278px;height:1px;background:var(--beige)}
.about .copy{position:absolute;left:594px;top:153px;width:545px;font-size:19px;line-height:23.5px;color:#2f2427}
.about .copy p+p{margin-top:23px}
.about .copy p.tight{margin-top:0}
.about .copy .accent{color:var(--wine)}

/* why */
.why{position:absolute;top:2157px;width:334px;height:226px}
.why.raised{background:var(--white);border-radius:10px;box-shadow:0 6px 22px rgba(67,22,36,.1)}
.why svg{position:absolute;left:27px;top:30px}
.why h3{position:absolute;left:27px;top:107px;font-family:'Playfair Display',serif;font-weight:400;font-size:23px;color:var(--aubergine)}
.why p{position:absolute;left:27px;top:146px;width:295px;font-size:12px;line-height:18px;color:var(--muted)}
.dot{position:absolute;top:2424px;width:16px;height:16px;border-radius:50%;background:#f0e3de}
.dot.on{background:var(--wine)}

/* contact */
.contact{left:0;top:2466px;width:1200px;height:523px;background:var(--cream)}
.contact-item{position:absolute;left:212px;display:flex;align-items:center;gap:22px;font-size:17px;line-height:23px;color:#2f2427}
.ci-icon{width:31px;height:31px;border-radius:50%;background:var(--orange);display:flex;align-items:center;justify-content:center;flex:none}
.field{position:absolute;background:var(--white);border:1.5px solid var(--field);border-radius:22px;font-size:11px;color:var(--wine);padding:18px 0 0 18px}
.field.message{border-radius:14px}

/* testimonials */
.t-label{left:240px;top:3084px;font-size:11px;letter-spacing:3px;color:var(--orange);font-weight:700}
.t-card{position:absolute;width:334px;height:236px;background:var(--white);border-radius:12px;box-shadow:0 6px 22px rgba(67,22,36,.08)}
.t-card .q{position:absolute;right:26px;top:-60px;font-family:'Playfair Display',serif;font-size:170px;line-height:170px;color:#f3dcd8}
.t-card h4{position:absolute;left:27px;top:40px;font-weight:400;font-size:19px;color:var(--text)}
.t-card p{position:absolute;left:27px;top:78px;width:215px;font-size:11.5px;line-height:16.5px;color:var(--muted)}
.t-card .avatar{position:absolute;left:27px;top:160px;width:54px;height:54px;border-radius:50%;background:#efe3e0}
.t-card .who{position:absolute;left:94px;top:171px;font-size:12px;color:#2f2427;line-height:15px}
.t-card .who small{display:block;font-size:9px;color:#2f2427}
.t-card .stars{position:absolute;right:28px;top:180px}
.arrow{position:absolute;width:57px;height:57px;border-radius:50%;display:flex;align-items:center;justify-content:center}

/* footer */
.footer{left:0;top:3690px;width:1200px;height:411px;background:var(--footer-bg)}
.footer-brand{position:absolute;left:49px;top:3800px;display:flex;align-items:center;gap:18px}
.footer-brand .mark{width:64px;height:64px;border-radius:50%;background:var(--wine);display:block}
.footer-brand .name{font-family:'Nunito',sans-serif;font-weight:800;font-size:44px;line-height:44px;color:var(--wine);letter-spacing:2px}
.f-head{position:absolute;top:3800px;font-family:'Playfair Display',serif;font-weight:600;font-size:19px;color:var(--aubergine)}
.f-rule{position:absolute;top:3841px;height:1.5px;background:var(--wine)}
.f-text{position:absolute;font-size:13px;line-height:17px;color:#2f2427}
.f-link{position:absolute;left:697px;font-size:16px;color:#2f2427}
.social{position:absolute;left:957px;display:flex;align-items:center;gap:18px;font-size:16px;color:#2f2427}
.social span.circle{width:35px;height:35px;border-radius:50%;background:var(--white);box-shadow:0 2px 6px rgba(0,0,0,.08);display:flex;align-items:center;justify-content:center}
.social span.circle i{width:14px;height:14px;border-radius:50%;background:var(--orange);display:block}
</style>
</head>
<body>

<!-- Header -->
<header>
  <div class="brand"><span class="brand-dot"></span><span class="brand-name">VORMI</span></div>
  <nav class="nav"><span class="active">Home</span><span>Workshop</span><span>Courses</span><span>Agenda</span><span>Travel</span></nav>
  <div class="btn btn-wine" style="left:1074px;top:32px;width:76px;height:38px;">Join</div>
</header>

<!-- Hero -->
<div class="abs hero" role="img" aria-label="Photo of a person sitting on a rock in a calm lake at sunset"></div>
<h1 class="hero-title">Advancement of People<br>and Organization</h1>
<p class="hero-sub">Develop yourself, together with VORMI — where personal<br>growth meets professional excellence.</p>
<div class="btn btn-wine" style="left:398px;top:532px;width:170px;height:47px;">For Individuals</div>
<div class="btn btn-orange" style="left:597px;top:532px;width:194px;height:47px;">For Organisations</div>

<!-- Services -->
<h2 class="h-center" style="top:720px;font-size:54px;font-weight:700;">Our Services</h2>
<p class="p-center" style="top:805px;">VORMI provides innovative programs designed to strengthen both individuals and<br>organizations. Explore our core offerings below.</p>

<div class="service" style="left:49px;">
  <div class="service-icon"><svg width="24" height="24" viewBox="0 0 24 24" fill="none" stroke="#fff" stroke-width="2"><rect x="6" y="3" width="12" height="18" rx="2"/><path d="M10 3v18"/></svg></div>
  <h3>Courses</h3>
  <p>Deep-dive learning programs that foster personal awareness and professional effectiveness.</p>
  <div class="more">View More</div>
</div>
<div class="service" style="left:329px;">
  <div class="service-icon"><svg width="26" height="24" viewBox="0 0 26 24" fill="#fff"><circle cx="13" cy="8" r="3.5"/><circle cx="5.5" cy="10" r="2.5"/><circle cx="20.5" cy="10" r="2.5"/><path d="M7 19c0-4 3-6 6-6s6 2 6 6z"/><path d="M1 19c0-3 2-5 4.5-5S9 15 9 16v3z"/><path d="M25 19c0-3-2-5-4.5-5S17 15 17 16v3z"/></svg></div>
  <h3>Workshops</h3>
  <p>Short, focused sessions that inspire immediate insight and action.</p>
  <div class="more">View More</div>
</div>
<div class="service" style="left:608px;">
  <div class="service-icon"><svg width="24" height="24" viewBox="0 0 24 24" fill="#fff"><path d="M21 3c-1-1-3 0-4 1l-4 4-8-2-2 2 6 4-3 3-3-1-1 1 4 2 2 4 1-1-1-3 3-3 4 6 2-2-2-8 4-4c1-1 2-3 1-4z"/></svg></div>
  <h3>Travel Experiences</h3>
  <p>Transformative journeys that combine learning, reflection, and adventure.</p>
  <div class="more">View More</div>
</div>
<div class="service" style="left:887px;">
  <div class="service-icon"><svg width="24" height="24" viewBox="0 0 24 24" fill="none" stroke="#fff" stroke-width="2"><rect x="3" y="4" width="18" height="14" rx="2"/><circle cx="10" cy="10" r="2.5"/><path d="M6 16c1-2 2.5-3 4-3s3 1 4 3M14 8h4M15 11h3"/></svg></div>
  <h3>Seminars</h3>
  <p>Expert-led sessions for teams and organizations seeking collective growth.</p>
  <div class="more">View More</div>
</div>

<div class="btn btn-wine" style="left:500px;top:1143px;width:186px;height:47px;">View Full Agenda</div>

<!-- About -->
<section class="abs about">
  <h2 class="serif">About Us</h2>
  <div class="rule"></div>
  <div class="copy">
    <p>At <span class="accent">VORMI</span>, our learning academy, we believe that true development begins with self-awareness and genuine connection.</p>
    <p>Our mission is to guide individuals and organizations toward personal insight, professional balance, and lasting transformation.</p>
    <p class="tight">Through our courses, workshops, and development journeys, we combine science-based learning with a holistic approach to human growth — creating experiences that inspire clarity, purpose, and collaboration.</p>
  </div>
</section>
<div class="abs about-photo" role="img" aria-label="Close-up photo of a pink water lily"></div>
<div class="btn btn-orange" style="left:594px;top:1733px;width:186px;height:48px;">View Full Agenda</div>

<!-- Why choose -->
<h2 class="h-center" style="top:1945px;font-size:56px;font-weight:400;">Why Choose <b style="font-weight:700;">VORMI</b></h2>
<p class="p-center" style="top:2052px;font-size:15.5px;line-height:23px;color:var(--muted);">Lorem Ipsum is simply dummy text of the printing and typesetting industry. Lorem Ipsum<br>has been the industry's standard dummy text ever since the 1500s,</p>

<div class="why" style="left:83px;">
  <svg width="60" height="60" viewBox="0 0 60 60" fill="none"><circle cx="38" cy="34" r="18" fill="#f6e4de"/><path d="M26 4l5 4 6-1 2 6 6 3-2 6 2 6-6 3-2 6-6-1-5 4-5-4-6 1-2-6-6-3 2-6-2-6 6-3 2-6 6 1z" stroke="#2f2427" stroke-width="2" transform="translate(0,4)"/><path d="M18 30l6 6 11-12" stroke="#2f2427" stroke-width="2.5"/></svg>
  <h3>Holistic Learning</h3>
  <p>We see development as a combination of knowledge, awareness, and experience.</p>
</div>
<div class="why raised" style="left:433px;">
  <svg width="60" height="60" viewBox="0 0 60 60" fill="none"><circle cx="38" cy="34" r="18" fill="#f6e4de"/><path d="M26 4l5 4 6-1 2 6 6 3-2 6 2 6-6 3-2 6-6-1-5 4-5-4-6 1-2-6-6-3 2-6-2-6 6-3 2-6 6 1z" stroke="#2f2427" stroke-width="2" transform="translate(0,4)"/><path d="M18 30l6 6 11-12" stroke="#2f2427" stroke-width="2.5"/></svg>
  <h3>Professional Expertise</h3>
  <p>Our trainers and coaches bring deep, real-world experience to every session.</p>
</div>
<div class="why" style="left:783px;">
  <svg width="60" height="60" viewBox="0 0 60 60" fill="none"><circle cx="38" cy="34" r="18" fill="#f6e4de"/><path d="M26 4l5 4 6-1 2 6 6 3-2 6 2 6-6 3-2 6-6-1-5 4-5-4-6 1-2-6-6-3 2-6-2-6 6-3 2-6 6 1z" stroke="#2f2427" stroke-width="2" transform="translate(0,4)"/><path d="M18 30l6 6 11-12" stroke="#2f2427" stroke-width="2.5"/></svg>
  <h3>Sustainable Growth</h3>
  <p>We help people and teams build long-lasting change — not quick fixes.</p>
</div>
<span class="dot on" style="left:546px;"></span>
<span class="dot" style="left:576px;"></span>
<span class="dot" style="left:606px;"></span>
<span class="dot" style="left:637px;"></span>

<!-- Contact -->
<section class="abs contact"></section>
<h2 class="abs serif" style="left:212px;top:2600px;font-size:40px;font-weight:700;color:var(--aubergine);">Contact Us</h2>
<div class="contact-item" style="top:2685px;"><span class="ci-icon"><svg width="14" height="16" viewBox="0 0 14 16" fill="#fff"><path d="M7 0a6 6 0 0 1 6 6c0 4-6 10-6 10S1 10 1 6a6 6 0 0 1 6-6zm0 4a2 2 0 1 0 0 4 2 2 0 0 0 0-4z"/></svg></span><span>Lindenhofstraat 14<br>8011 KP Zwolle</span></div>
<div class="contact-item" style="top:2757px;"><span class="ci-icon"><svg width="14" height="14" viewBox="0 0 14 14" fill="#fff"><path d="M3 0l3 3-2 2c1 2 3 4 5 5l2-2 3 3-2 3C6 14 0 8 0 3z"/></svg></span><span>038 412 5596</span></div>
<div class="contact-item" style="top:2818px;"><span class="ci-icon"><svg width="14" height="11" viewBox="0 0 14 11" fill="none" stroke="#fff" stroke-width="1.6"><rect x="1" y="1" width="12" height="9" rx="1"/><path d="M1 2l6 4 6-4"/></svg></span><span>info@vormi.nl</span></div>

<h2 class="abs serif" style="left:648px;top:2538px;font-size:34px;font-weight:700;color:var(--aubergine);">Fill The Form</h2>
<div class="field" style="left:648px;top:2618px;width:204px;height:53px;">First Name</div>
<div class="field" style="left:864px;top:2618px;width:204px;height:53px;">Last Name</div>
<div class="field" style="left:648px;top:2679px;width:204px;height:53px;">Phone No.</div>
<div class="field" style="left:864px;top:2679px;width:204px;height:53px;">Email Add</div>
<div class="field message" style="left:648px;top:2742px;width:420px;height:112px;">Message</div>
<div class="btn btn-wine" style="left:648px;top:2897px;width:188px;height:48px;">View Full Agenda</div>

<!-- Testimonials -->
<div class="abs t-label">TRUST OUR &nbsp;CLIENTS</div>
<h2 class="abs serif" style="left:237px;top:3106px;font-size:40px;font-weight:700;color:var(--aubergine);">Testimonials</h2>
<p class="abs" style="left:241px;top:3180px;font-size:12px;line-height:18px;color:#2f2427;">Lorem Ipsum is simply dummy text<br>of the typesetting industry.</p>
<div class="arrow" style="left:241px;top:3267px;background:var(--white);box-shadow:0 3px 10px rgba(0,0,0,.1);"><svg width="20" height="16" viewBox="0 0 20 16" fill="none" stroke="#2f2427" stroke-width="2.2"><path d="M19 8H2M8 2L2 8l6 6"/></svg></div>
<div class="arrow" style="left:313px;top:3267px;background:var(--wine);"><svg width="20" height="16" viewBox="0 0 20 16" fill="none" stroke="#fff" stroke-width="2.2"><path d="M1 8h17M12 2l6 6-6 6"/></svg></div>

<div class="t-card" style="left:627px;top:3072px;">
  <span class="q">“</span>
  <h4>Lorem Ipsum text</h4>
  <p>Lorem Ipsum is simply dummy text of the typesetting industry.Lorem Ipsum is simply dummy text of the typesetting industry.</p>
  <span class="avatar"></span>
  <span class="who">John Smith<small>Manager</small></span>
  <svg class="stars" width="102" height="16" viewBox="0 0 102 16" fill="#F26C2E"><g id="s"><path d="M8 0l2.4 5 5.6.6-4.2 3.8 1.2 5.6L8 12.2 3 15l1.2-5.6L0 5.6 5.6 5z"/></g><use href="#s" x="21"/><use href="#s" x="42"/><use href="#s" x="63"/><use href="#s" x="84"/></svg>
</div>
<div class="t-card" style="left:240px;top:3366px;">
  <span class="q">“</span>
  <h4>Lorem Ipsum text</h4>
  <p>Lorem Ipsum is simply dummy text of the typesetting industry.Lorem Ipsum is simply dummy text of the typesetting industry.</p>
  <span class="avatar"></span>
  <span class="who">John Smith<small>Manager</small></span>
  <svg class="stars" width="102" height="16" viewBox="0 0 102 16" fill="#F26C2E"><use href="#s"/><use href="#s" x="21"/><use href="#s" x="42"/><use href="#s" x="63"/><use href="#s" x="84"/></svg>
</div>
<div class="t-card" style="left:627px;top:3366px;">
  <span class="q">“</span>
  <h4>Lorem Ipsum text</h4>
  <p>Lorem Ipsum is simply dummy text of the typesetting industry.Lorem Ipsum is simply dummy text of the typesetting industry.</p>
  <span class="avatar"></span>
  <span class="who">John Smith<small>Manager</small></span>
  <svg class="stars" width="102" height="16" viewBox="0 0 102 16" fill="#F26C2E"><use href="#s"/><use href="#s" x="21"/><use href="#s" x="42"/><use href="#s" x="63"/><use href="#s" x="84"/></svg>
</div>

<!-- Footer -->
<div class="abs footer"></div>
<svg class="abs" style="left:0;top:3630px;" width="1200" height="120" viewBox="0 0 1200 120">
  <path d="M0 120V60C90 20 200 10 330 30C480 55 560 90 700 100C780 106 850 104 900 100C780 118 650 110 520 90C380 68 250 60 130 78C80 86 35 100 0 120Z" fill="#750E2B"/>
  <path d="M0 120C35 100 80 86 130 78C250 60 380 68 520 90C650 110 780 118 900 100C1010 88 1110 70 1200 60V120Z" fill="#f7eeea"/>
</svg>

<div class="footer-brand"><span class="mark"></span><span class="name">VORMI</span></div>
<p class="f-text" style="left:49px;top:3917px;">Lorem Ipsum is simply dummy text<br>of the typesetting industry.</p>
<p class="f-text" style="left:49px;top:4052px;font-size:12px;">© Company- All Rights Reserved</p>

<div class="f-head" style="left:406px;">Contact Us</div>
<div class="f-rule" style="left:406px;width:158px;"></div>
<div class="abs" style="left:406px;top:3868px;display:flex;gap:20px;align-items:center;"><span class="ci-icon"><svg width="14" height="16" viewBox="0 0 14 16" fill="#fff"><path d="M7 0a6 6 0 0 1 6 6c0 4-6 10-6 10S1 10 1 6a6 6 0 0 1 6-6zm0 4a2 2 0 1 0 0 4 2 2 0 0 0 0-4z"/></svg></span><span style="font-size:12.5px;line-height:17px;">Lindenhofstraat 14<br>8011 KP Zwolle</span></div>
<div class="abs" style="left:406px;top:3932px;display:flex;gap:20px;align-items:center;"><span class="ci-icon"><svg width="14" height="14" viewBox="0 0 14 14" fill="#fff"><path d="M3 0l3 3-2 2c1 2 3 4 5 5l2-2 3 3-2 3C6 14 0 8 0 3z"/></svg></span><span style="font-size:12.5px;">038 412 5596</span></div>
<div class="abs" style="left:406px;top:3995px;display:flex;gap:20px;align-items:center;"><span class="ci-icon"><svg width="14" height="11" viewBox="0 0 14 11" fill="none" stroke="#fff" stroke-width="1.6"><rect x="1" y="1" width="12" height="9" rx="1"/><path d="M1 2l6 4 6-4"/></svg></span><span style="font-size:12.5px;">info@vormi.nl</span></div>

<div class="f-head" style="left:689px;">Quick Link</div>
<div class="f-rule" style="left:689px;width:165px;"></div>
<span class="f-link" style="top:3870px;">Home</span>
<span class="f-link" style="top:3904px;">Course</span>
<span class="f-link" style="top:3938px;">Workshop</span>
<span class="f-link" style="top:3972px;">Agenda</span>
<span class="f-link" style="top:4006px;">Travel</span>

<div class="f-head" style="left:957px;top:3795px;">Follow &nbsp;Us</div>
<div class="f-rule" style="left:957px;width:160px;"></div>
<div class="social" style="top:3866px;"><span class="circle"><i></i></span>Snapvale</div>
<div class="social" style="top:3922px;"><span class="circle"><i></i></span>Postwire</div>
<div class="social" style="top:3978px;"><span class="circle"><i></i></span>Circlehub</div>

</body>
</html>
```